Payroll Brochure

Create a brochure with the copy i have provided . A simple easy tp read brochure that shows wat we do we handle payroll taxes insurance 401k etc

```html
<!DOCTYPE html>
<html lang="en">
<head>
<meta charset="utf-8">
<title>Norvale Payroll Brochure</title>
<link href="https://fonts.googleapis.com/css2?family=Montserrat:wght@500;700;800&family=Open+Sans:wght@400;600&display=swap" rel="stylesheet">
<style>
  :root {
    --maroon: #7a1a1f;
    --maroon-deep: #4f0d12;
    --gold: #c8903f;
    --gold-light: #e2b16a;
    --paper: #ffffff;
    --ink: #3a3a3a;
    --muted: #7b7b7b;
    --stage: #5a5a5a;
  }
  * { box-sizing: border-box; margin: 0; padding: 0; }
  html, body { width: 1200px; height: 2516px; overflow: hidden; }
  body {
    background: var(--stage);
    font-family: "Open Sans", Arial, sans-serif;
    color: var(--ink);
    display: flex;
    flex-direction: column;
  }
  .view { flex: 1; display: flex; align-items: center; justify-content: center; }
  .spread { display: flex; box-shadow: 0 12px 30px rgba(0,0,0,.35); }
  .page {
    position: relative;
    width: 520px;
    height: 736px;
    background: var(--paper);
    overflow: hidden;
  }
  .view--cover .page { box-shadow: 0 12px 30px rgba(0,0,0,.35); }
  .art { position: absolute; inset: 0; width: 100%; height: 100%; }

  /* Cover */
  .cover-head {
    position: absolute; top: 44px; right: 30px; width: 220px; text-align: right;
    font-family: "Montserrat", Arial, sans-serif;
  }
  .cover-kicker { color: var(--gold); font-weight: 700; font-size: 22px; letter-spacing: 1px; }
  .cover-title { color: var(--maroon); font-weight: 800; font-size: 27px; line-height: 1.1; }
  .cover-sub { font-family: "Open Sans", Arial, sans-serif; font-size: 10.5px; color: var(--muted); margin-top: 8px; line-height: 1.45; }
  .brand {
    position: absolute; display: flex; align-items: center; gap: 8px;
    font-family: "Montserrat", Arial, sans-serif; font-weight: 800; color: var(--maroon);
  }
  .cover .brand { left: 250px; top: 620px; font-size: 30px; }
  .brand-mark { width: 22px; height: 22px; background: var(--gold); }

  /* Back panel */
  .back { background: linear-gradient(160deg, var(--maroon-deep) 0%, var(--maroon) 55%, #94262b 100%); color: #fff; }
  .back-title {
    position: absolute; left: 40px; top: 300px; width: 300px;
    font-family: "Montserrat", Arial, sans-serif; font-weight: 800; font-size: 30px; line-height: 1.1;
  }
  .back-rule { position: absolute; left: 40px; top: 378px; width: 60px; height: 3px; background: var(--gold); }
  .back-copy { position: absolute; left: 40px; top: 396px; width: 420px; font-size: 11px; line-height: 1.6; color: #f1dcdc; }
  .back-contact {
    position: absolute; left: 40px; right: 40px; bottom: 50px; display: flex; justify-content: space-between;
    font-size: 11px; font-weight: 600; color: #fff; border-top: 1px solid rgba(255,255,255,.35); padding-top: 12px;
  }

  /* Inside */
  .inside-left .brand { left: 290px; top: 156px; font-size: 22px; }
  .inside-left .brand .brand-mark { width: 16px; height: 16px; }
  .feature-grid {
    position: absolute; left: 34px; right: 30px; top: 440px;
    display: grid; grid-template-columns: 1fr 1fr; gap: 26px 28px;
  }
  .feature h3, .service h3 {
    font-family: "Montserrat", Arial, sans-serif; font-weight: 800; font-size: 12px;
    color: var(--maroon); letter-spacing: .5px; margin-bottom: 6px;
  }
  .feature p, .service p { font-size: 9px; line-height: 1.55; color: var(--muted); }
  .page-foot { position: absolute; left: 0; right: 0; bottom: 0; height: 14px; background: var(--maroon); }
  .page-foot::after { content: ""; position: absolute; left: 0; top: -4px; width: 40%; height: 4px; background: var(--gold); }

  .spine-badge {
    position: absolute; left: 4px; top: 138px; width: 104px;
    font-family: "Montserrat", Arial, sans-serif; font-weight: 700; font-size: 10.5px; color: #fff;
    line-height: 1.45; text-align: center;
  }
  .tab-label {
    position: absolute; right: 16px; top: 70px; font-family: "Montserrat", Arial, sans-serif;
    font-weight: 800; font-size: 14px; color: #fff; letter-spacing: 1px;
  }
  .service-list { position: absolute; left: 150px; top: 40px; width: 200px; }
  .service { margin-bottom: 22px; }
  .service-band {
    position: absolute; left: 110px; right: 0; top: 292px; height: 30px; background: var(--maroon);
    color: #fff; font-family: "Montserrat", Arial, sans-serif; font-weight: 800; font-size: 12px;
    display: flex; align-items: center; padding-left: 40px; letter-spacing: .5px;
  }
  .service-lower { position: absolute; left: 150px; top: 346px; width: 210px; }
</style>
</head>
<body>

<!-- Front cover -->
<section class="view view--cover">
  <article class="page cover">
    <svg class="art" viewBox="0 0 520 736">
      <defs>
        <linearGradient id="maroonFill" x1="0" y1="0" x2="1" y2="1">
          <stop offset="0" stop-color="#4f0d12"/><stop offset="1" stop-color="#8e2328"/>
        </linearGradient>
        <linearGradient id="photoFill" x1="0" y1="0" x2="1" y2="1">
          <stop offset="0" stop-color="#e4e7ea"/><stop offset="1" stop-color="#8e969f"/>
        </linearGradient>
      </defs>
      <polygon points="0,0 230,0 0,300" fill="url(#maroonFill)"/>
      <polygon points="0,470 0,600 300,736 440,736" fill="url(#maroonFill)"/>
      <g role="img" aria-label="Photo of two business people shaking hands">
        <rect x="60" y="190" width="280" height="280" rx="46" transform="rotate(45 200 330)" fill="url(#photoFill)" stroke="#c8903f" stroke-width="9"/>
      </g>
    </svg>
    <div class="cover-head">
      <p class="cover-kicker">LOREM IPSUM</p>
      <h1 class="cover-title">DOLOR SIT AMET</h1>
      <p class="cover-sub">Payroll, taxes, insurance and 401k handled for you, accurately and on time, every period.</p>
    </div>
    <div class="brand"><span class="brand-mark"></span><span class="brand-name">NORVALE</span></div>
  </article>
</section>

<!-- Outside spread -->
<section class="view">
  <div class="spread">
    <article class="page back">
      <h2 class="back-title">THE NORVALE ADVANTAGE</h2>
      <span class="back-rule"></span>
      <p class="back-copy">We take payroll off your desk so you can focus on running your business. Our team processes every pay run, files payroll taxes, manages workers' compensation and benefits, and keeps your 401k contributions in order. One partner, one point of contact, and clear reports you can trust.</p>
      <div class="back-contact"><span>(555) 010-2846</span><span>www.norvalepayroll.com</span></div>
    </article>
    <article class="page cover">
      <svg class="art" viewBox="0 0 520 736">
        <defs>
          <linearGradient id="maroonFill2" x1="0" y1="0" x2="1" y2="1">
            <stop offset="0" stop-color="#4f0d12"/><stop offset="1" stop-color="#8e2328"/>
          </linearGradient>
          <linearGradient id="photoFill2" x1="0" y1="0" x2="1" y2="1">
            <stop offset="0" stop-color="#e4e7ea"/><stop offset="1" stop-color="#8e969f"/>
          </linearGradient>
        </defs>
        <polygon points="0,0 230,0 0,300" fill="url(#maroonFill2)"/>
        <polygon points="0,470 0,600 300,736 440,736" fill="url(#maroonFill2)"/>
        <g role="img" aria-label="Photo of two business people shaking hands">
          <rect x="60" y="190" width="280" height="280" rx="46" transform="rotate(45 200 330)" fill="url(#photoFill2)" stroke="#c8903f" stroke-width="9"/>
        </g>
      </svg>
      <div class="cover-head">
        <p class="cover-kicker">LOREM IPSUM</p>
        <h1 class="cover-title">DOLOR SIT AMET</h1>
        <p class="cover-sub">Payroll, taxes, insurance and 401k handled for you, accurately and on time, every period.</p>
      </div>
      <div class="brand"><span class="brand-mark"></span><span class="brand-name">NORVALE</span></div>
    </article>
  </div>
</section>

<!-- Inside spread -->
<section class="view">
  <div class="spread">
    <article class="page inside-left">
      <svg class="art" viewBox="0 0 520 736">
        <defs>
          <linearGradient id="photoFill3" x1="0" y1="0" x2="1" y2="1">
            <stop offset="0" stop-color="#dfe4ea"/><stop offset="1" stop-color="#7d8793"/>
          </linearGradient>
        </defs>
        <g role="img" aria-label="Photo of a team reviewing documents at a desk">
          <circle cx="140" cy="170" r="120" fill="url(#photoFill3)" stroke="#c8903f" stroke-width="8"/>
        </g>
      </svg>
      <div class="brand"><span class="brand-mark"></span><span class="brand-name">NORVALE</span></div>
      <div class="feature-grid">
        <div class="feature"><h3>PRICING</h3><p>Simple flat rates per employee with no hidden fees, so you always know what payroll will cost each month.</p></div>
        <div class="feature"><h3>SERVICE</h3><p>A dedicated specialist answers your questions and handles every change quickly and personally.</p></div>
        <div class="feature"><h3>PRODUCTS</h3><p>Payroll, tax filing, workers' comp, health insurance and 401k plans, all from one provider.</p></div>
        <div class="feature"><h3>FLEXIBILITY</h3><p>Weekly, biweekly or monthly runs, direct deposit or checks, tailored to your team.</p></div>
      </div>
      <div class="page-foot"></div>
    </article>
    <article class="page inside-right">
      <svg class="art" viewBox="0 0 520 736">
        <defs>
          <linearGradient id="goldFill" x1="0" y1="0" x2="1" y2="1">
            <stop offset="0" stop-color="#e2b16a"/><stop offset="1" stop-color="#8a4a22"/>
          </linearGradient>
          <linearGradient id="photoFill4" x1="0" y1="0" x2="1" y2="1">
            <stop offset="0" stop-color="#e2e6ea"/><stop offset="1" stop-color="#6f7a88"/>
          </linearGradient>
        </defs>
        <rect x="-70" y="80" width="170" height="170" rx="16" transform="rotate(45 15 165)" fill="url(#goldFill)"/>
        <polygon points="320,0 520,0 520,260" fill="#7a1a1f"/>
        <g role="img" aria-label="Photo of a smiling businessman">
          <circle cx="430" cy="640" r="80" fill="url(#photoFill4)" stroke="#c8903f" stroke-width="7"/>
        </g>
      </svg>
      <p class="spine-badge">WE HANDLE<br>YOUR PAYROLL<br>SO YOU DON'T</p>
      <p class="tab-label">PAYROLL</p>
      <div class="service-list">
        <div class="service"><h3>FLEXIBLE</h3><p>Pay schedules and reports that fit the way your business already works.</p></div>
        <div class="service"><h3>EFFICIENT</h3><p>Submit hours in minutes and let us take care of the rest.</p></div>
        <div class="service"><h3>GROW WITHOUT GROWING PAINS</h3><p>Add staff and locations without adding paperwork.</p></div>
      </div>
      <div class="service-band">TAX, INSURANCE &amp; 401K</div>
      <div class="service-lower">
        <div class="service"><h3>ACCURATE</h3><p>Every deduction and filing checked before it leaves our office.</p></div>
        <div class="service"><h3>COMPLETE</h3><p>Taxes, insurance and retirement plans managed together in one place.</p></div>
      </div>
      <div class="page-foot"></div>
    </article>
  </div>
</section>

</body>
</html>
```